" Atendimento personalizado as necessidades do cliente em todos os ramos de tradução. Assistência 24h com plataforma online. Garantindo a segurança de toda documentação pela QTR, Pex, Velkor. "

```html
<!DOCTYPE html>
<html lang="pt-BR">
<head>
<meta charset="utf-8">
<title>Lumeral Traduções – Cartão de visita</title>
<link rel="stylesheet" href="https://fonts.googleapis.com/css2?family=Cinzel:wght@600&family=Roboto+Condensed:wght@400&family=Raleway:wght@400&display=swap">
<style>
  :root {
    --page-bg: #e9ebee;
    --navy: #1f3a5f;
    --navy-deep: #182f4d;
    --sky: #6cc4f0;
    --ink: #1c2a3d;
    --muted: #9fb4cc;
    --card-light: #ffffff;
    --card-shade: #e4e7eb;
  }
  * { margin: 0; padding: 0; box-sizing: border-box; }
  html, body { width: 1200px; height: 1200px; overflow: hidden; }
  body { background: var(--page-bg); position: relative; }

  .business-card {
    position: absolute;
    left: 96px; top: 360px;
    width: 1008px; height: 396px;
    background: radial-gradient(ellipse at 60% 40%, var(--card-light) 40%, var(--card-shade) 100%);
    overflow: hidden;
    box-shadow: 0 6px 18px rgba(0,0,0,0.18);
  }
  .brand-panel { position: absolute; inset: 0; width: 100%; height: 100%; }

  .brand {
    position: absolute;
    left: 24px; top: 104px;
    width: 300px;
    text-align: center;
  }
  .brand-mark {
    display: block;
    width: 80px; height: 80px;
    margin: 0 auto 16px;
    border-radius: 50%;
    background: var(--sky);
  }
  .brand-name {
    font-family: "Cinzel", serif;
    font-weight: 600;
    font-size: 50px;
    line-height: 1;
    color: #ffffff;
  }
  .brand-tagline {
    margin-top: 10px;
    font-family: "Raleway", sans-serif;
    font-size: 14px;
    letter-spacing: 9px;
    padding-left: 9px;
    color: var(--muted);
  }

  .contact-list {
    position: absolute;
    left: 520px; top: 44px;
    list-style: none;
    font-family: "Roboto Condensed", sans-serif;
    font-size: 24px;
    color: var(--ink);
  }
  .contact-item { display: flex; align-items: flex-start; margin-bottom: 22px; }
  .contact-item svg { flex: none; width: 34px; height: 34px; margin-right: 12px; }
  .contact-item.address svg { margin-left: -32px; }
  .contact-item p { line-height: 29px; }

  .website {
    position: absolute;
    left: 458px; top: 305px;
    font-family: "Roboto Condensed", sans-serif;
    font-size: 44px;
    color: var(--ink);
  }
</style>
</head>
<body>
  <div class="business-card">
    <svg class="brand-panel" viewBox="0 0 1008 396" preserveAspectRatio="none" aria-hidden="true">
      <polygon points="0,0 434,0 338,396 0,396" fill="var(--sky)"/>
      <polygon points="0,0 410,0 314,396 0,396" fill="var(--navy)"/>
    </svg>

    <div class="brand">
      <span class="brand-mark" aria-hidden="true"></span>
      <div class="brand-name">LUMERAL</div>
      <div class="brand-tagline">TRADUÇÕES</div>
    </div>

    <ul class="contact-list">
      <li class="contact-item phone">
        <svg viewBox="0 0 34 34" aria-hidden="true">
          <circle cx="17" cy="17" r="14" fill="var(--navy-deep)"/>
          <rect x="12.5" y="9" width="9" height="16" rx="2" fill="none" stroke="#fff" stroke-width="2"/>
          <circle cx="17" cy="22" r="1" fill="#fff"/>
        </svg>
        <p>99 9 9999 99 99 | 9999 99 99</p>
      </li>
      <li class="contact-item email">
        <svg viewBox="0 0 34 34" aria-hidden="true">
          <circle cx="17" cy="17" r="14" fill="var(--navy-deep)"/>
          <rect x="10" y="12" width="14" height="10" rx="1" fill="none" stroke="#fff" stroke-width="2"/>
          <polyline points="10,12 17,18 24,12" fill="none" stroke="#fff" stroke-width="2"/>
        </svg>
        <p>contato@lumeral.com.br</p>
      </li>
      <li class="contact-item address">
        <svg viewBox="0 0 34 34" aria-hidden="true">
          <path d="M17 3 C10 3 6 8 6 13 C6 21 17 31 17 31 C17 31 28 21 28 13 C28 8 24 3 17 3 Z" fill="var(--navy-deep)"/>
          <circle cx="17" cy="13" r="4" fill="#fff"/>
        </svg>
        <p>Rua do Lumeral, 9999 | Centro<br>Sala 1000 - CEP: 55.555-555<br>Cidade - UF</p>
      </li>
    </ul>

    <div class="website">www.LUMERAL.com.br</div>
  </div>
</body>
</html>
```